Small corporate website template design

I need a couple templates designed for a small corporate website. The corporate site reflects the existence of the parent company which will own various brands/services that have their own websites, so it will mainly be used to present who we are, what we do, what is happening (news/events), how to contact us, link off to our other brand/service sites, as well as post information for public relations, investors, and job opportunities.

The company name is Velmoranth LLC (www.velmoranth-example.com), and the name is representative of stratified layers of interconnected digital services. The corporate site is not expected to generate a bunch of fanfare - that honor will be reserved for the externally linked brand/service sites.

The provided logo may be manipulated in color, size, shape, positioning, etc. to get it to fit with the design, but should be integrated in some way.

What we are looking for is a home page layout as well as a template for an inner page whereby the navigation/logo, etc may be diminished to some extent for the inner pages. We are also interested in reusable elements such as dividers, content containers, etc. in order to represent the types of information described above that we would like to present as described above.

We are particularly interested in consistency of design elements, conservative use of color (including consideration of accessibility concerns), judicious use of whitespace in favor of simplified messaging, and something lending itself well to internationalization/translation.

Target Market(s)

Small business owners, entrepreneurs (B2B)

Number of Pages Required

2 page

Font styles to use
Sans Serif

Requirements
Must have
• See the attached PDF with the logo concept, color swatches, and comparative sites.

```html
<!DOCTYPE html>
<html lang="en">
<head>
<meta charset="utf-8">
<title>Velmoranth LLC</title>
<link rel="stylesheet" href="https://fonts.googleapis.com/css2?family=Open+Sans:ital,wght@0,400;0,600;0,700;1,400&family=Questrial&display=swap">
<style>
:root{
  --hero-bright:#0b34e0;
  --hero-deep:#021056;
  --hero-night:#010a35;
  --navy:#0b1f86;
  --navy-text:#0b2596;
  --ink:#2a2a2a;
  --muted:#666;
  --cyan:#0aaee8;
  --band:#02062a;
  --white:#fff;
  --social:#1d58b8;
}
*{box-sizing:border-box;margin:0;padding:0}
html,body{width:1200px;height:2236px;overflow:hidden}
body{position:relative;font-family:"Open Sans",Arial,sans-serif;color:var(--ink);background:var(--white)}
.abs{position:absolute}

/* Hero */
.hero{position:absolute;left:0;top:0;width:1200px;height:580px;
  background:radial-gradient(ellipse at 15% 30%,var(--hero-bright) 0%,#0726b0 35%,var(--hero-deep) 75%,var(--hero-night) 100%);overflow:hidden}
.hero-curve{position:absolute;left:0;top:0}
.brand-mark{position:absolute;left:166px;top:22px;font-family:"Open Sans",sans-serif;font-weight:700;font-size:22px;color:var(--white);display:flex;align-items:center;gap:8px}
.brand-mark .dot{width:14px;height:14px;border-radius:50%;background:var(--white)}
.nav{position:absolute;top:24px;left:576px;display:flex;gap:44px}
.nav a{color:var(--white);text-decoration:none;font-size:19px;font-weight:600}
.hero-title{position:absolute;top:132px;left:0;width:1200px;text-align:center;font-family:"Questrial",sans-serif;font-size:27px;color:var(--white);letter-spacing:1px}
.card{position:absolute;box-shadow:0 8px 18px rgba(0,0,0,.45);overflow:hidden}
.card .pic{position:absolute;left:0;top:0;width:100%}
.card .label{position:absolute;left:0;bottom:0;width:100%;background:var(--cyan);color:var(--white);text-align:center;padding:8px 10px 6px}
.card .label h3{font-size:17px;font-weight:600;letter-spacing:.5px}
.card .label p{font-size:10px;line-height:1.2}
.card.lead .label{background:#0a0c1c}

/* Intro */
.intro-col{position:absolute;top:574px;width:440px;text-align:center}
.intro-col .icon{width:46px;height:46px;border-radius:50%;background:var(--navy);margin:0 auto;display:flex;align-items:center;justify-content:center}
.intro-col h2{margin-top:30px;font-size:24px;font-weight:400;color:#333;letter-spacing:.5px}
.intro-col h2 span{color:var(--navy-text)}
.intro-col p{margin-top:22px;font-size:16.5px;line-height:1.6;color:var(--muted)}
.btn{display:inline-block;margin-top:16px;width:112px;height:30px;line-height:30px;border-radius:6px;background:var(--navy);color:var(--white);font-size:13px;font-weight:600;text-decoration:none}

/* Feature band */
.feature{position:absolute;left:0;top:870px;width:1200px;height:318px}
.feature-copy{position:absolute;left:0;top:0;width:663px;height:318px;background:linear-gradient(90deg,var(--band) 0%,#061a6e 70%,#0a2aa8 100%)}
.feature-copy h2{position:absolute;left:164px;top:62px;color:var(--white);font-size:26px;font-weight:700;line-height:1.4;letter-spacing:.5px}
.feature-copy p{position:absolute;left:164px;top:148px;width:420px;color:var(--white);font-size:14.5px;line-height:1.8}
.btn-ghost{position:absolute;left:160px;top:250px;width:108px;height:29px;border:1.5px solid var(--white);border-radius:15px;color:var(--white);font-size:14px;text-align:center;line-height:26px;text-decoration:none}
.feature-media{position:absolute;left:663px;top:0;width:537px;height:318px;background:radial-gradient(ellipse at 45% 55%,#d9cfc6 0%,#8c8f99 40%,#3a4a66 80%,#24304a 100%)}

/* Blog */
.blog-head{position:absolute;top:1232px;left:0;width:1200px;text-align:center;font-size:31px;font-weight:600;color:#222}
.blog-lede{position:absolute;top:1280px;left:395px;width:410px;text-align:center;font-size:14px;line-height:1.85;color:var(--muted)}
.post{position:absolute;top:1382px;width:264px}
.post .pic{width:264px;height:162px}
.post h3{margin-top:14px;font-size:16px;font-weight:600;color:#555}
.post p{margin-top:8px;font-size:10.5px;line-height:1.75;color:#444}
.arrow{position:absolute;top:1452px}

/* Services */
.services{position:absolute;left:0;top:1704px;width:1200px;height:214px;background:var(--band)}
.services h2{position:absolute;top:18px;width:1200px;text-align:center;color:var(--white);font-size:21px;font-weight:400}
.service{position:absolute;top:114px;transform:translateY(-50%);display:flex;align-items:center;gap:7px;color:#c9c9c9;font-family:"Open Sans",sans-serif;font-weight:600;font-size:17px;letter-spacing:1px}
.service .sq{width:12px;height:12px;background:#c9c9c9}
.dots{position:absolute;top:174px;left:581px;display:flex;gap:14px}
.dots span{width:4px;height:4px;border-radius:50%;background:#555}
.dots span.on{background:#ccc}

/* Footer */
.footer-brand{position:absolute;left:168px;top:1958px;font-weight:700;font-size:20px;color:#111;display:flex;align-items:center;gap:7px}
.footer-brand .dot{width:12px;height:12px;border-radius:50%;background:#111}
.contact{position:absolute;left:170px;top:2018px;font-style:italic;font-size:15px;color:#111;line-height:1.45}
.contact h4{font-weight:400;font-style:italic;font-size:15px;margin-bottom:24px;text-transform:uppercase}
.contact .phone{margin-top:22px}
.fcol{position:absolute;top:1986px}
.fcol h4{font-size:15px;font-weight:400;color:#111;margin-bottom:20px}
.fcol ul{list-style:none}
.fcol li{font-size:13px;font-weight:600;color:#111;line-height:25.5px}
.fcol .two{display:flex;gap:40px}
.social{display:flex;gap:11px;margin-top:6px}
.social span{width:30px;height:30px;background:var(--social)}
</style>
</head>
<body>

<header class="hero">
  <svg class="hero-curve" width="1200" height="580" viewBox="0 0 1200 580" aria-hidden="true">
    <path d="M0 120 C300 40 600 10 820 0" stroke="rgba(150,190,255,.35)" stroke-width="2" fill="none"/>
    <path d="M700 300 C850 230 1000 220 1200 240" stroke="rgba(120,170,255,.35)" stroke-width="2" fill="none"/>
    <path d="M0 574 C260 500 700 460 1200 492 L1200 580 L0 580 Z" fill="#fff"/>
  </svg>
  <div class="brand-mark"><span class="dot"></span>Velmoranth</div>
  <nav class="nav"><a href="#">About</a><a href="#">Our Services</a><a href="#">News</a><a href="#">Contact Us</a></nav>
  <h1 class="hero-title">Adaptive Software Technology for the Digital Revolution</h1>
</header>

<div class="card" style="left:230px;top:279px;width:140px;height:229px">
  <div class="pic" role="img" aria-label="Globe and technology visual" style="height:150px;background:linear-gradient(160deg,#7fb6c8,#1d4c66 60%,#0a1f33)"></div>
  <div class="label" style="height:79px"><h3>BRAND 4</h3><p>Lorem ipsum dolor sit amet, consectetur adipiscing elit, sed do</p></div>
</div>
<div class="card" style="left:838px;top:285px;width:132px;height:217px">
  <div class="pic" role="img" aria-label="Person at a desk visual" style="height:140px;background:linear-gradient(160deg,#dfe8e8,#9fb7b8 60%,#5f7a80)"></div>
  <div class="label" style="height:77px"><h3>BRAND 5</h3><p>Lorem ipsum dolor sit amet, consectetur adipiscing elit, sed do</p></div>
</div>
<div class="card" style="left:370px;top:262px;width:143px;height:260px">
  <div class="pic" role="img" aria-label="Red car at speed visual" style="height:180px;background:linear-gradient(160deg,#0c4050,#3a5a50 45%,#a03a1a 75%,#2a0a05)"></div>
  <div class="label" style="height:80px"><h3>BRAND 2</h3><p>Lorem ipsum dolor sit amet, consectetur adipiscing elit, sed do</p></div>
</div>
<div class="card" style="left:698px;top:262px;width:140px;height:260px">
  <div class="pic" role="img" aria-label="Floating media objects visual" style="height:180px;background:linear-gradient(160deg,#0a1630,#1a3a78 50%,#c0623a 80%,#4a3a70)"></div>
  <div class="label" style="height:80px"><h3>BRAND 3</h3><p>Lorem ipsum dolor sit amet, consectetur adipiscing elit, sed do</p></div>
</div>
<div class="card lead" style="left:513px;top:246px;width:185px;height:297px">
  <div class="pic" role="img" aria-label="Hand touching digital icons visual" style="height:225px;background:radial-gradient(ellipse at 50% 60%,#c79a96,#5a4a66 45%,#1e1a30 90%)"></div>
  <div class="label" style="height:72px"><h3>BRAND 1</h3><p>Lorem ipsum dolor sit amet, consectetur adipiscing elit, sed do</p></div>
</div>

<section class="intro-col" style="left:140px">
  <div class="icon"><svg width="24" height="24" viewBox="0 0 24 24" aria-hidden="true"><rect x="6" y="6" width="12" height="12" fill="none" stroke="#fff" stroke-width="1.8"/><path d="M9 2v4M15 2v4M9 18v4M15 18v4M2 9h4M2 15h4M18 9h4M18 15h4" stroke="#fff" stroke-width="1.6"/></svg></div>
  <h2>WHO IS <span>VELMORANTH LLC</span>?</h2>
  <p>Lorem ipsum dolor sit amet, consectetur adipiscing elit. Aenean euismod bibendum laoreet. Proin gravida dolor sit amet lacus accumsan et viverra justo commodo.</p>
  <a class="btn" href="#">About us</a>
</section>
<section class="intro-col" style="left:621px">
  <div class="icon"><svg width="24" height="24" viewBox="0 0 24 24" aria-hidden="true"><circle cx="12" cy="12" r="8" fill="none" stroke="#fff" stroke-width="1.8"/><circle cx="12" cy="12" r="3.5" fill="none" stroke="#fff" stroke-width="1.6"/><path d="M12 12l7-7" stroke="#fff" stroke-width="1.6"/></svg></div>
  <h2>WHAT WE <span>DO</span>?</h2>
  <p>Lorem ipsum dolor sit amet, consectetur adipiscing elit. Aenean euismod bibendum laoreet. Proin gravida dolor sit amet lacus accumsan et viverra justo commodo.</p>
  <a class="btn" href="#">Our Services</a>
</section>

<section class="feature">
  <div class="feature-copy">
    <h2>DIGITAL LAYERS TO RAISE<br>THE QUALITY OF LIFE</h2>
    <p>Lorem ipsum dolor sit amet, consectetur adipiscing elit. Aenean euismod bibendum laoreet. Proin gravida dolor sit amet lacus accumsan et viverra justo commodo.</p>
    <a class="btn-ghost" href="#">Purchase</a>
  </div>
  <div class="feature-media" role="img" aria-label="Video still of a person wearing a virtual reality headset">
    <svg class="abs" style="left:242px;top:133px" width="52" height="52" viewBox="0 0 52 52" aria-hidden="true"><circle cx="26" cy="26" r="24" fill="rgba(0,0,0,.15)" stroke="#fff" stroke-width="2"/><path d="M21 16l15 10-15 10z" fill="#fff"/></svg>
  </div>
</section>

<h2 class="blog-head">Stories on the blog.</h2>
<p class="blog-lede">Lorem ipsum dolor sit amet, consectetur adipiscing elit. Aenean euismod bibendum laoreet. Proin gravida dolor sit amet lacus accumsan et viverra justo commodo.</p>
<svg class="arrow" style="left:148px" width="14" height="24" viewBox="0 0 14 24" aria-hidden="true"><path d="M12 2L3 12l9 10" stroke="#555" stroke-width="3" fill="none"/></svg>
<svg class="arrow" style="left:1040px" width="14" height="24" viewBox="0 0 14 24" aria-hidden="true"><path d="M2 2l9 10-9 10" stroke="#555" stroke-width="3" fill="none"/></svg>
<article class="post" style="left:188px">
  <div class="pic" role="img" aria-label="Person wearing smart glasses" style="background:linear-gradient(110deg,#b9a79a,#d8d4d0 45%,#8a8f98)"></div>
  <h3>Title</h3>
  <p>Lorem ipsum dolor sit amet, consectetur adipiscing elit. Aenean euismod bibendum laoreet. Proin gravida dolor sit amet lacus accumsan et viverra justo commodo.</p>
</article>
<article class="post" style="left:468px">
  <div class="pic" role="img" aria-label="Gadgets: game console, phone, camera and drone" style="background:linear-gradient(110deg,#1a2238,#3a3f55 40%,#2a2a30 70%,#6a1a3a)"></div>
  <h3>Title</h3>
  <p>Lorem ipsum dolor sit amet, consectetur adipiscing elit. Aenean euismod bibendum laoreet. Proin gravida dolor sit amet lacus accumsan et viverra justo commodo.</p>
</article>
<article class="post" style="left:750px">
  <div class="pic" role="img" aria-label="Hand wearing a smart ring device" style="background:linear-gradient(110deg,#2a2a2e,#6a5a55 50%,#1a1a1e)"></div>
  <h3>Title</h3>
  <p>Lorem ipsum dolor sit amet, consectetur adipiscing elit. Aenean euismod bibendum laoreet. Proin gravida dolor sit amet lacus accumsan et viverra justo commodo.</p>
</article>

<section class="services">
  <h2>Our other services</h2>
  <div class="service" style="left:172px"><span class="sq"></span>ORBEL</div>
  <div class="service" style="left:320px">TALLHAVEN</div>
  <div class="service" style="left:484px">CORVANE</div>
  <div class="service" style="left:632px">NIGHTFOLD</div>
  <div class="service" style="left:790px">BRIXLEY</div>
  <div class="service" style="left:944px"><span class="sq"></span>ROUTEWISE</div>
  <div class="dots"><span></span><span class="on"></span><span></span></div>
</section>

<footer>
  <div class="footer-brand"><span class="dot"></span>Velmoranth</div>
  <div class="contact">
    <h4>Contact</h4>
    Velmoranth LLC<br>Address1<br>Address2
    <div class="phone">0800 555 0142</div>
  </div>
  <div class="fcol" style="left:380px">
    <h4>PRODUCTS</h4>
    <div class="two">
      <ul><li>Payments</li><li>Billing</li><li>Connect</li><li>Sigma</li><li>Atlas</li><li>Radar</li></ul>
      <ul><li>Pricing</li><li>Global</li><li>Guides</li></ul>
    </div>
  </div>
  <div class="fcol" style="left:632px">
    <h4>COMPANY</h4>
    <ul><li>About</li><li>Customers</li><li>Jobs</li><li>Blog</li><li>Environment</li></ul>
  </div>
  <div class="fcol" style="left:792px">
    <h4>RESOURCES</h4>
    <ul><li>Support</li><li>Contact</li><li>Privacy &amp; terms</li><li>Sitemap</li></ul>
  </div>
  <div class="fcol" style="left:954px;top:1993px">
    <h4>CONNECT WITH US</h4>
    <div class="social"><span aria-label="Social link 1"></span><span aria-label="Social link 2"></span><span aria-label="Social link 3"></span><span aria-label="Social link 4"></span></div>
  </div>
</footer>

</body>
</html>
```